Funky new Serviced Apartment Company needs a website + logo

Bright Nest Serviced Accommodation is a new company aiming to attract customers who need temporary accommodation (2 days to 6 months) in city locations.

Our customers make considerable savings on longer stays compared to hotels, and have all the creature comforts of home including super-fast WIFI, comfy beds, full kitchen and modern, yet comfortable, furniture.

Another key feature of the design is a page to attract "Partners" who "Work with Us" by allowing us to manage their properties and becoming part of our network of accommodation units. I have include a brochure from one of our competitors, and a video can be found here: http://lnkvault-example.com/aptclip-7 - both can be used as I have permission.

The website design should work on all devices and screen sizes, and lend itself to a mobile app.

We would like to see website designs that are modern and simple, with a strong brand logo. The final design should communicate "Home From Home" and aim to attract professionals away from home on business for long periods of time.

Target Market(s)

Professional People working away from home for extended periods of time

Industry/Entity Type

Accommodation

Contact Information for Business Card

Name, Title, Phone Number, Email
Callum Fenwick, Owner, 07831 552907, callum.fenwick@brightnestsa-example.co.uk

Logo Text

Bright Nest Service Accommodation (Serviced Accommodation optional)

Coding

Coded - Design and coding required

Number of Pages Required

3 page

Font styles to use
Sans Serif

Requirements
Must have
• A 3 page website: Home, Partners, Contact Us
• Home page should have an area to list current apartment units, the user should be able to select a location and filter the list based on price and number of people.
• Partners page should inspire a "Work with us" call to action.
• The design should work with all screen sizes and devices.
• The design should say friendly and professional
Nice to have
• A simple logo, perhaps a smiling face made up using letters 'W' and 'H'.
• A neutral color scheme
Should not have
• No garish or vivid color scheme

```html
<!DOCTYPE html>
<html lang="en">
<head>
<meta charset="utf-8">
<title>Bright Nest – Serviced Apartments</title>
<link href="https://fonts.googleapis.com/css2?family=Poppins:wght@400;500;600;700&family=Open+Sans:wght@400;600&display=swap" rel="stylesheet">
<style>
:root{
  --accent:#f0485a;
  --violet:#8a63f2;
  --violet-dark:#6a46e0;
  --ink:#1d1d1f;
  --text:#555a60;
  --muted:#9a9ea4;
  --line:#e8e8ea;
  --panel:#f4f4f6;
  --footer:#1c1f28;
  --footer-deep:#161820;
  --white:#ffffff;
}
*{box-sizing:border-box;margin:0;padding:0}
html,body{width:1200px;height:2880px;overflow:hidden}
body{position:relative;background:var(--white);font-family:"Open Sans",Arial,sans-serif;color:var(--text)}
.abs{position:absolute}

/* top bar */
.topbar{left:0;top:0;width:1200px;height:30px;background:#f5f5f6;font-size:11px;color:#555}
.topbar .item{top:8px;display:flex;align-items:center;gap:8px}
.topbar .socials{right:190px;top:8px;display:flex;gap:22px}
.topbar .socials span{width:12px;height:12px;border-radius:50%;background:#c4c6cb;display:block}
.topbar .login{right:88px;top:7px;color:var(--accent);font-weight:600;display:flex;gap:8px;align-items:center}
.topbar .divider{right:165px;top:6px;width:1px;height:18px;background:#ddd}

/* header */
.header{left:0;top:30px;width:1200px;height:95px;background:var(--white)}
.logo{left:88px;top:32px;display:flex;align-items:center;gap:10px;font-family:"Poppins",Arial,sans-serif;font-weight:600;font-size:24px;color:var(--ink)}
.logo .mark{width:22px;height:22px;background:var(--accent);border-radius:50%}
.nav{right:132px;top:40px;display:flex;gap:30px;font-family:"Poppins",Arial,sans-serif;font-size:12px;color:#333}
.nav .active{color:var(--violet)}
.nav-tick{left:759px;top:0;width:0;height:0;border-left:7px solid transparent;border-right:7px solid transparent;border-top:7px solid var(--violet)}
.search{right:88px;top:36px}

/* hero */
.hero{left:0;top:125px;width:1200px;height:591px;background:linear-gradient(180deg,#8a9bb0 0%,#5b4a3e 35%,#8a6444 60%,#3f4a2e 100%)}
.hero-title{left:0;width:1200px;top:208px;text-align:center;font-family:"Poppins",Arial,sans-serif;font-weight:700;font-size:50px;line-height:60px;color:var(--white)}
.hero-sub{left:340px;width:520px;top:272px;text-align:center;font-size:14px;line-height:22px;color:var(--white)}
.btn-white{background:var(--white);color:var(--ink);font-family:"Poppins",Arial,sans-serif;font-size:11px;font-weight:600;text-align:center}
.hero-btn{left:518px;top:330px;width:148px;height:44px;line-height:44px}
.hero-arrow{top:282px;width:26px;height:46px;background:var(--white);display:flex;align-items:center;justify-content:center}
.explore{left:0;width:1200px;top:527px;text-align:center;color:var(--white);font-family:"Poppins",Arial,sans-serif;font-size:10px;font-weight:600}

/* units */
.section-title{left:0;width:1200px;text-align:center;font-family:"Poppins",Arial,sans-serif;font-weight:500;font-size:28px;color:var(--ink)}
.filter{left:230px;top:839px;width:740px;height:115px;background:var(--panel)}
.filter .field{top:26px}
.filter label{display:block;font-size:12px;color:#333;margin-bottom:8px}
.filter .select{width:174px;height:46px;background:var(--white);font-size:10px;color:var(--muted);padding:0 16px;display:flex;align-items:center;justify-content:space-between}
.filter .go{left:584px;top:47px;width:130px;height:46px;background:var(--accent);color:var(--white);font-family:"Poppins",Arial,sans-serif;font-size:10px;font-weight:600;line-height:46px;text-align:center}

.card{width:327px}
.card .photo{width:327px;height:230px}
.card h3{font-family:"Poppins",Arial,sans-serif;font-weight:500;font-size:15px;color:var(--ink);margin:22px 0 16px 16px}
.card .meta{display:flex;align-items:center;gap:10px;margin:0 0 10px 16px;font-size:11px;color:#777}
.card .more{display:flex;align-items:center;gap:8px;margin:18px 0 0 16px;font-family:"Poppins",Arial,sans-serif;font-size:10px;color:#444}

/* get in touch */
.cta{left:0;top:1840px;width:1200px;height:295px;background:linear-gradient(90deg,#8a5cf5 0%,#9a78f0 50%,#8d67f4 100%)}
.cta h2{top:60px;left:0;width:1200px;text-align:center;font-family:"Poppins",Arial,sans-serif;font-weight:500;font-size:28px;color:var(--white)}
.cta p{top:120px;left:180px;width:840px;text-align:center;font-size:13px;line-height:22px;color:var(--white)}
.cta .btn-white{left:522px;top:184px;width:156px;height:48px;line-height:48px}

/* testimonials */
.stars{left:0;width:1200px;top:2256px;text-align:center;color:#f2a23a;font-size:17px;letter-spacing:3px}
.quote{left:210px;width:780px;top:2282px;text-align:center;font-size:13px;line-height:22px;color:#888}
.client{left:0;width:1200px;top:2338px;text-align:center;color:var(--accent);font-family:"Poppins",Arial,sans-serif;font-size:13px}
.avatars{left:410px;top:2385px;display:flex;gap:24px}
.avatars span{width:56px;height:56px;border-radius:50%;display:block}

/* footer */
.footer{left:0;top:2508px;width:1200px;height:330px;background:var(--footer);color:#c9cbd1;font-size:11px}
.footer h4{font-family:"Poppins",Arial,sans-serif;font-weight:500;font-size:15px;color:var(--white);margin-bottom:24px}
.footer .col{top:60px}
.footer ul{list-style:none}
.footer li{margin-bottom:17px}
.footer .rule{top:70px;width:1px;height:200px;background:#2c303b}
.footer .contact li{display:flex;gap:14px;align-items:flex-start;line-height:17px;margin-bottom:20px}
.round{width:30px;height:30px;border-radius:50%;background:#2e323d;display:inline-block}
.card-chip{width:44px;height:28px;border-radius:3px;display:inline-block}
.copy{left:0;top:2838px;width:1200px;height:42px;background:var(--footer-deep);color:#d8d9dd;font-size:11px;text-align:center;line-height:42px}
.totop{right:28px;top:2834px;width:40px;height:40px;border-radius:50%;background:var(--accent);display:flex;align-items:center;justify-content:center}
</style>
</head>
<body>

<div class="abs topbar">
  <div class="abs item" style="left:88px">
    <svg width="12" height="12" viewBox="0 0 24 24"><path d="M6.6 10.8a15 15 0 0 0 6.6 6.6l2.2-2.2a1 1 0 0 1 1-.25 11 11 0 0 0 3.6.6 1 1 0 0 1 1 1V20a1 1 0 0 1-1 1A17 17 0 0 1 3 4a1 1 0 0 1 1-1h3.5a1 1 0 0 1 1 1 11 11 0 0 0 .6 3.6 1 1 0 0 1-.25 1z" fill="#aaa"/></svg>
    +08 555 0182 446
  </div>
  <div class="abs item" style="left:256px">
    <svg width="13" height="10" viewBox="0 0 26 20"><rect x="1" y="1" width="24" height="18" fill="none" stroke="#aaa" stroke-width="2"/><path d="M1 1l12 10L25 1" fill="none" stroke="#aaa" stroke-width="2"/></svg>
    hello@brightnest-example.com
  </div>
  <div class="abs socials"><span></span><span></span><span></span><span></span><span></span></div>
  <div class="abs divider"></div>
  <div class="abs login">
    <svg width="11" height="12" viewBox="0 0 22 24"><circle cx="11" cy="6" r="5" fill="#f0485a"/><path d="M1 24c0-7 4-10 10-10s10 3 10 10z" fill="#f0485a"/></svg>
    LOGIN
  </div>
</div>

<header class="abs header">
  <div class="abs nav-tick"></div>
  <div class="abs logo"><span class="mark"></span>Bright Nest</div>
  <nav class="abs nav">
    <span class="active">HOME</span><span>ABOUT US</span><span>PARTNERS</span><span>CONTACT US</span>
  </nav>
  <svg class="abs search" width="22" height="22" viewBox="0 0 22 22"><circle cx="9" cy="9" r="7" fill="none" stroke="#999" stroke-width="1.6"/><path d="M14 14l6 6" stroke="#999" stroke-width="1.6"/></svg>
</header>

<section class="abs hero" role="img" aria-label="Photograph of a curved modern apartment building with wraparound balconies at dusk">
  <h1 class="abs hero-title">Welcome To Appartments</h1>
  <p class="abs hero-sub">This is a placeholder version of Lorem Ipsum proin gravida nibh vel velit auctor aliquet. Aenean sollicitudin lorem quis bibendum auctor.</p>
  <div class="abs btn-white hero-btn">WORK WITH US</div>
  <div class="abs hero-arrow" style="left:0;width:24px"><svg width="8" height="12" viewBox="0 0 8 12"><path d="M7 1L2 6l5 5" fill="none" stroke="#333" stroke-width="2"/></svg></div>
  <div class="abs hero-arrow" style="right:0"><svg width="8" height="12" viewBox="0 0 8 12"><path d="M1 1l5 5-5 5" fill="none" stroke="#333" stroke-width="2"/></svg></div>
  <div class="abs explore">EXPLORE<br>
    <svg width="18" height="22" viewBox="0 0 18 22" style="margin-top:4px"><path d="M9 1v19M2 13l7 7 7-7" fill="none" stroke="#fff" stroke-width="2"/></svg>
  </div>
</section>

<h2 class="abs section-title" style="top:778px">Current Appartment Units</h2>

<form class="abs filter">
  <div class="abs field" style="left:27px"><label>Location :</label><div class="select">Select Location <span>⌄</span></div></div>
  <div class="abs field" style="left:212px"><label>Price :</label><div class="select">Select Price <span>⌄</span></div></div>
  <div class="abs field" style="left:396px"><label>Number of People :</label><div class="select">Select number of people <span>⌄</span></div></div>
  <div class="abs go">FILTER BASED</div>
</form>

<article class="abs card" style="left:88px;top:991px">
  <div class="photo" role="img" aria-label="Bedroom with a white double bed and warm wooden wall" style="background:linear-gradient(135deg,#d8b49a,#efe7df 60%,#3d3a3a)"></div>
  <h3>Appartment Name Goes Here...</h3>
  <div class="meta"><svg width="9" height="12" viewBox="0 0 12 16"><path d="M6 0a6 6 0 0 0-6 6c0 4.5 6 10 6 10s6-5.5 6-10a6 6 0 0 0-6-6zm0 8.5A2.5 2.5 0 1 1 6 3.5a2.5 2.5 0 0 1 0 5z" fill="#f0485a"/></svg>Some Address line goes City name Australia</div>
  <div class="meta"><svg width="10" height="11" viewBox="0 0 22 24"><circle cx="11" cy="6" r="5" fill="#f0485a"/><path d="M1 24c0-7 4-10 10-10s10 3 10 10z" fill="#f0485a"/></svg>10 Person Allowed in Appartments</div>
  <div class="more">VIEW APPARTMENTS <svg width="14" height="10" viewBox="0 0 14 10"><path d="M0 5h12M8 1l4 4-4 4" fill="none" stroke="#444" stroke-width="1.3"/></svg></div>
</article>

<article class="abs card" style="left:436px;top:991px">
  <div class="photo" role="img" aria-label="Bright room with lime green bedding and a green rug" style="background:linear-gradient(135deg,#e6ecd8,#f4f6f0 45%,#9bc43a)"></div>
  <h3>Appartment Name Goes Here...</h3>
  <div class="meta"><svg width="9" height="12" viewBox="0 0 12 16"><path d="M6 0a6 6 0 0 0-6 6c0 4.5 6 10 6 10s6-5.5 6-10a6 6 0 0 0-6-6zm0 8.5A2.5 2.5 0 1 1 6 3.5a2.5 2.5 0 0 1 0 5z" fill="#f0485a"/></svg>Some Address line goes City name New York</div>
  <div class="meta"><svg width="10" height="11" viewBox="0 0 22 24"><circle cx="11" cy="6" r="5" fill="#f0485a"/><path d="M1 24c0-7 4-10 10-10s10 3 10 10z" fill="#f0485a"/></svg>15 Person Allowed in Appartments</div>
  <div class="more">VIEW APPARTMENTS <svg width="14" height="10" viewBox="0 0 14 10"><path d="M0 5h12M8 1l4 4-4 4" fill="none" stroke="#444" stroke-width="1.3"/></svg></div>
</article>

<article class="abs card" style="left:783px;top:991px">
  <div class="photo" role="img" aria-label="Bedside with an amber lamp and white bed linen" style="background:linear-gradient(135deg,#c8783a,#6a4a30 40%,#efe8dc 75%)"></div>
  <h3>Appartment Name Goes Here...</h3>
  <div class="meta"><svg width="9" height="12" viewBox="0 0 12 16"><path d="M6 0a6 6 0 0 0-6 6c0 4.5 6 10 6 10s6-5.5 6-10a6 6 0 0 0-6-6zm0 8.5A2.5 2.5 0 1 1 6 3.5a2.5 2.5 0 0 1 0 5z" fill="#f0485a"/></svg>Some Address line goes City name Brazil</div>
  <div class="meta"><svg width="10" height="11" viewBox="0 0 22 24"><circle cx="11" cy="6" r="5" fill="#f0485a"/><path d="M1 24c0-7 4-10 10-10s10 3 10 10z" fill="#f0485a"/></svg>05 Person Allowed in Appartments</div>
  <div class="more">VIEW APPARTMENTS <svg width="14" height="10" viewBox="0 0 14 10"><path d="M0 5h12M8 1l4 4-4 4" fill="none" stroke="#444" stroke-width="1.3"/></svg></div>
</article>

<article class="abs card" style="left:88px;top:1398px">
  <div class="photo" role="img" aria-label="Airy bedroom with sheer curtains and a grey rug" style="background:linear-gradient(135deg,#c7ccd4,#eef0f2 50%,#8a8688)"></div>
  <h3>Appartment Name Goes Here...</h3>
  <div class="meta"><svg width="9" height="12" viewBox="0 0 12 16"><path d="M6 0a6 6 0 0 0-6 6c0 4.5 6 10 6 10s6-5.5 6-10a6 6 0 0 0-6-6zm0 8.5A2.5 2.5 0 1 1 6 3.5a2.5 2.5 0 0 1 0 5z" fill="#f0485a"/></svg>Some Address line goes City name Thailand</div>
  <div class="meta"><svg width="10" height="11" viewBox="0 0 22 24"><circle cx="11" cy="6" r="5" fill="#f0485a"/><path d="M1 24c0-7 4-10 10-10s10 3 10 10z" fill="#f0485a"/></svg>07 Person Allowed in Appartments</div>
  <div class="more">VIEW APPARTMENTS <svg width="14" height="10" viewBox="0 0 14 10"><path d="M0 5h12M8 1l4 4-4 4" fill="none" stroke="#444" stroke-width="1.3"/></svg></div>
</article>

<article class="abs card" style="left:436px;top:1398px">
  <div class="photo" role="img" aria-label="Living room with a white sofa and window blinds" style="background:linear-gradient(135deg,#9a9ca0,#e4e6e8 50%,#b4b6ba)"></div>
  <h3>Appartment Name Goes Here...</h3>
  <div class="meta"><svg width="9" height="12" viewBox="0 0 12 16"><path d="M6 0a6 6 0 0 0-6 6c0 4.5 6 10 6 10s6-5.5 6-10a6 6 0 0 0-6-6zm0 8.5A2.5 2.5 0 1 1 6 3.5a2.5 2.5 0 0 1 0 5z" fill="#f0485a"/></svg>Some Address line goes City name Ubited States</div>
  <div class="meta"><svg width="10" height="11" viewBox="0 0 22 24"><circle cx="11" cy="6" r="5" fill="#f0485a"/><path d="M1 24c0-7 4-10 10-10s10 3 10 10z" fill="#f0485a"/></svg>03 Person Allowed in Appartments</div>
  <div class="more" style="color:#222">VIEW APPARTMENTS <svg width="14" height="10" viewBox="0 0 14 10"><path d="M0 5h12M8 1l4 4-4 4" fill="none" stroke="#222" stroke-width="1.3"/></svg></div>
</article>

<article class="abs card" style="left:783px;top:1398px">
  <div class="photo" role="img" aria-label="Cream bedroom with olive curtains and a beige rug" style="background:linear-gradient(135deg,#7a7a2c,#efe6d2 45%,#d9c6a4)"></div>
  <h3>Appartment Name Goes Here...</h3>
  <div class="meta"><svg width="9" height="12" viewBox="0 0 12 16"><path d="M6 0a6 6 0 0 0-6 6c0 4.5 6 10 6 10s6-5.5 6-10a6 6 0 0 0-6-6zm0 8.5A2.5 2.5 0 1 1 6 3.5a2.5 2.5 0 0 1 0 5z" fill="#f0485a"/></svg>Some Address line goes City name Malaysia</div>
  <div class="meta"><svg width="10" height="11" viewBox="0 0 22 24"><circle cx="11" cy="6" r="5" fill="#f0485a"/><path d="M1 24c0-7 4-10 10-10s10 3 10 10z" fill="#f0485a"/></svg>06 Person Allowed in Appartments</div>
  <div class="more">VIEW APPARTMENTS <svg width="14" height="10" viewBox="0 0 14 10"><path d="M0 5h12M8 1l4 4-4 4" fill="none" stroke="#444" stroke-width="1.3"/></svg></div>
</article>

<section class="abs cta" role="img" aria-label="Violet tinted photograph of an apartment interior">
  <h2 class="abs">The First Thing To Do is Get in Touch</h2>
  <p class="abs">Morbi accumsan ipsum velit nam nec tellus a odio tincidunt auctor a ornare odio Sed non mauris vitae erat consequat auctor eu in elit. Class aptent taciti sociosqu ad litora torquent per conubia nostra per inceptos himenaeos Mauris in erat justo</p>
  <div class="abs btn-white">GET IN TOUCH</div>
</section>

<h2 class="abs section-title" style="top:2198px">Client's Testimonials</h2>
<div class="abs stars">★★★★★</div>
<p class="abs quote">Lorem ipsum dolor sit amet consectetuer adipiscing elit aenean commodo ligula eget dolor aenean massa cum sociis natoque penatibus et magnis dis parturient montes nascetur ridiculus mus donec quam felis ultricies nec...</p>
<div class="abs client">MARLA QUINBY</div>
<div class="abs avatars">
  <span role="img" aria-label="Client portrait" style="background:#e9e6e2;box-shadow:0 4px 10px rgba(0,0,0,.2)"></span>
  <span role="img" aria-label="Client portrait" style="background:#2e2a28"></span>
  <span role="img" aria-label="Client portrait" style="background:#e8b48c"></span>
  <span role="img" aria-label="Client portrait" style="background:#2c4a5e"></span>
  <span role="img" aria-label="Client portrait" style="background:#7fc1e6"></span>
</div>

<footer class="abs footer">
  <div class="abs col" style="left:88px">
    <h4>Quick Links</h4>
    <ul><li>Home</li><li>About Us</li><li>Partners</li><li>Contact Us</li><li>Work With Us</li></ul>
  </div>
  <div class="abs rule" style="left:278px"></div>
  <div class="abs col" style="left:359px">
    <h4>Information</h4>
    <ul><li>Appartments</li><li>Customers</li><li>Service</li><li>Terms &amp; Condition</li><li>Privacy Policy</li></ul>
  </div>
  <div class="abs rule" style="left:536px"></div>
  <div class="abs col contact" style="left:614px">
    <h4>Contact Details</h4>
    <ul>
      <li><svg width="10" height="13" viewBox="0 0 12 16"><path d="M6 0a6 6 0 0 0-6 6c0 4.5 6 10 6 10s6-5.5 6-10a6 6 0 0 0-6-6zm0 8.5A2.5 2.5 0 1 1 6 3.5a2.5 2.5 0 0 1 0 5z" fill="#f0485a"/></svg><span>Some address line goes here,<br>City name, Country name.</span></li>
      <li><svg width="11" height="11" viewBox="0 0 24 24"><path d="M6.6 10.8a15 15 0 0 0 6.6 6.6l2.2-2.2a1 1 0 0 1 1-.25 11 11 0 0 0 3.6.6 1 1 0 0 1 1 1V20a1 1 0 0 1-1 1A17 17 0 0 1 3 4a1 1 0 0 1 1-1h3.5a1 1 0 0 1 1 1 11 11 0 0 0 .6 3.6 1 1 0 0 1-.25 1z" fill="#f0485a"/></svg>(08) 555-014-2287</li>
      <li><svg width="12" height="10" viewBox="0 0 26 20"><rect x="0" y="0" width="26" height="20" fill="#f0485a"/><path d="M1 1l12 10L25 1" fill="none" stroke="#1c1f28" stroke-width="2"/></svg>stay@brightnest-example.com</li>
      <li><svg width="11" height="11" viewBox="0 0 22 22"><circle cx="11" cy="11" r="10" fill="#f0485a"/><rect x="6" y="8" width="10" height="7" fill="#1c1f28"/></svg>(08) 555-014-2287</li>
    </ul>
  </div>
  <div class="abs rule" style="left:826px"></div>
  <div class="abs col" style="left:904px">
    <h4>Follow Us</h4>
    <div style="display:flex;gap:14px;margin-bottom:28px"><span class="round"></span><span class="round"></span><span class="round"></span><span class="round"></span><span class="round"></span></div>
    <h4>Payment Methods</h4>
    <div style="display:flex;gap:8px"><span class="card-chip" style="background:#2a47c4"></span><span class="card-chip" style="background:#ffffff"></span><span class="card-chip" style="background:#2f7fd1"></span></div>
  </div>
</footer>
<div class="abs copy">©copyright 2017 &nbsp;|&nbsp; All Rights Reserved</div>
<div class="abs totop"><svg width="12" height="8" viewBox="0 0 12 8"><path d="M1 7l5-5 5 5" fill="none" stroke="#fff" stroke-width="2"/></svg></div>

</body>
</html>
```